Creative, Fun, Eye catching signage for new office - inspire and inform!

I am looking for a billboard sign, a smaller sign and a very small sign for parking spots. These will be located in our new office space. I have uploaded two logos, this way you can choose. I would love to see what it looks like with black behind the logo but am open to creative ideas. I would like the majority of the background to be black and/or white

1. Sign for over door – with five at the top like in the photo attached

The sign size is 2600mm (L) x 900mm (H)

Logo at the top then services to the right side
Social & Living Skills Programs
Support Workers
Respite/Supported Holidays
Exercise Physiology
Occupational Therapy
Speech Therapy
Psychology
Behavioural Therapy

I would like the design to tie in with the website and/or flyers/banners attached. Please also try and add 1800 527 930

2. Sign for glass roller door

745cm wide by 725cm high ( similar to what next door has without it saying parent )

Tallbrook Logo
Drop Off Zone

Smaller signs for parking spots
1000cm wide, 60cm high

Tallbrook logo Visitor Parking 24/7

I would like the design to be consistent across the three items so they work together but are not identical.

I have attached images showing what I am talking about in relation to the location of each sign.

Target Market(s)

Families, parents and people with disabilities

Industry/Entity Type

Disability and community service

Colors

Designer to choose colors to be used in the design.

Requirements
Must have
• White or black background - the logo and please use colours shown in the brochures and banners provided. Preferences are black white and yellow
Nice to have
• all of our services and website and/or 1800 527 930 on banner 1
Should not have
• I dont want it to be to busy please

```html
<!DOCTYPE html>
<html lang="en">
<head>
<meta charset="utf-8">
<title>Tallbrook Office Signage</title>
<link rel="stylesheet" href="https://fonts.googleapis.com/css2?family=Poppins:wght@400;500;700;800&display=swap">
<style>
  :root {
    --backdrop: #a29d99;
    --sign-white: #ffffff;
    --brand-yellow: #fbd920;
    --ink: #111111;
    --shadow: rgba(0,0,0,0.35);
  }
  * { margin: 0; padding: 0; box-sizing: border-box; }
  html, body { width: 696px; height: 1200px; overflow: hidden; }
  body {
    position: relative;
    background: var(--backdrop);
    font-family: "Poppins", sans-serif;
    color: var(--ink);
  }

  /* Brand name block */
  .brand { display: flex; flex-direction: column; align-items: center; }
  .brand-dot { background: var(--brand-yellow); border-radius: 50%; }
  .brand-name { font-family: "Poppins", sans-serif; font-weight: 700; color: var(--ink); line-height: 1; }

  /* Over-door sign */
  .door-sign { position: absolute; left: 65px; top: 360px; width: 567px; height: 196px; }
  .door-sign .number-tab {
    position: absolute; left: 249px; top: -38px; width: 69px; height: 69px;
    border-radius: 50%; background: var(--sign-white);
    display: flex; justify-content: center; padding-top: 8px;
    font-weight: 800; font-size: 26px; line-height: 1;
  }
  .door-sign .panel {
    position: absolute; inset: 0; background: var(--sign-white);
    box-shadow: 0 12px 10px -6px var(--shadow);
  }
  .door-sign .brand { position: absolute; left: 0; right: 0; top: 14px; }
  .door-sign .brand-dot { width: 26px; height: 26px; margin-bottom: 6px; }
  .door-sign .brand-name { font-size: 30px; }
  .services { position: absolute; top: 94px; list-style: none; }
  .services.left { left: 60px; }
  .services.right { left: 364px; }
  .services li {
    display: flex; align-items: center; gap: 5px;
    font-size: 11px; font-weight: 500; height: 19px;
  }
  .svc-icon { width: 12px; height: 12px; flex: none; }
  .contact-band {
    position: absolute; left: 0; right: 0; bottom: 0; height: 23px;
    background: var(--brand-yellow); border-top: 1.5px solid var(--ink);
    display: flex; align-items: center; font-size: 10px;
  }
  .contact-item { position: absolute; display: flex; align-items: center; gap: 6px; }
  .contact-item.phone { left: 126px; }
  .contact-item.web { left: 306px; }
  .contact-icon { width: 13px; height: 13px; }

  /* Visitor parking strip */
  .parking-strip {
    position: absolute; left: 66px; top: 620px; width: 567px; height: 34px;
    box-shadow: 0 10px 8px -6px var(--shadow);
  }
  .parking-strip svg { position: absolute; inset: 0; }
  .parking-strip .brand { position: absolute; left: 150px; top: 4px; width: 70px; }
  .parking-strip .brand-dot { width: 9px; height: 9px; margin-bottom: 2px; }
  .parking-strip .brand-name { font-size: 12px; }
  .parking-title {
    position: absolute; left: 238px; top: 6px;
    font-weight: 700; font-size: 17px; line-height: 1; white-space: nowrap;
  }

  /* Drop-off sign */
  .dropoff-sign {
    position: absolute; left: 260px; top: 718px; width: 176px; height: 171px;
    background: var(--sign-white); box-shadow: 0 12px 10px -6px var(--shadow);
  }
  .dropoff-sign .yellow-half {
    position: absolute; left: 0; right: 0; top: 91px; bottom: 0; background: var(--brand-yellow);
  }
  .dropoff-sign .frame { position: absolute; inset: 4px; border: 2px solid var(--ink); }
  .dropoff-sign .brand { position: absolute; left: 0; right: 0; top: 20px; }
  .dropoff-sign .brand-dot { width: 24px; height: 24px; margin-bottom: 6px; }
  .dropoff-sign .brand-name { font-size: 27px; }
  .dropoff-title {
    position: absolute; left: 0; right: 0; top: 100px; text-align: center;
    font-weight: 800; font-size: 25px; line-height: 1.18;
  }
</style>
</head>
<body>

<section class="door-sign">
  <div class="panel"></div>
  <div class="number-tab">5</div>
  <div class="brand">
    <span class="brand-dot"></span>
    <span class="brand-name">Tallbrook</span>
  </div>
  <ul class="services left">
    <li><svg class="svc-icon" viewBox="0 0 12 12"><circle cx="6" cy="6" r="6" fill="#111"/><circle cx="4" cy="5" r="1.3" fill="#fff"/><circle cx="8" cy="5" r="1.3" fill="#fff"/><rect x="2.5" y="7" width="7" height="2" rx="1" fill="#fff"/></svg>Social &amp; Living Skills Programs</li>
    <li><svg class="svc-icon" viewBox="0 0 12 12"><circle cx="6" cy="6" r="6" fill="#111"/><circle cx="6" cy="4.6" r="1.8" fill="none" stroke="#fff"/><path d="M3 9.5a3 3 0 0 1 6 0" fill="none" stroke="#fff"/></svg>Support Workers</li>
    <li><svg class="svc-icon" viewBox="0 0 12 12"><circle cx="6" cy="6" r="6" fill="#111"/><path d="M3 9l4-5 2 1" fill="none" stroke="#fff"/></svg>Respite/Supported Holidays</li>
    <li><svg class="svc-icon" viewBox="0 0 12 12"><circle cx="6" cy="6" r="6" fill="#111"/><circle cx="6" cy="3.5" r="1" fill="#fff"/><path d="M6 5v3l-2 1.5M6 8l2 1.5" fill="none" stroke="#fff"/></svg>Exercise Physiology</li>
  </ul>
  <ul class="services right">
    <li><svg class="svc-icon" viewBox="0 0 12 12"><circle cx="6" cy="6" r="6" fill="#111"/><circle cx="6" cy="3.5" r="1" fill="#fff"/><path d="M3 8h6M6 5v3" fill="none" stroke="#fff"/></svg>Occupational Therapy</li>
    <li><svg class="svc-icon" viewBox="0 0 12 12"><circle cx="6" cy="6" r="6" fill="#111"/><circle cx="6" cy="6" r="3" fill="#fff"/></svg>Speech Therapy</li>
    <li><svg class="svc-icon" viewBox="0 0 12 12"><circle cx="6" cy="6" r="6" fill="#111"/><ellipse cx="6" cy="6" rx="3.2" ry="2.4" fill="none" stroke="#fff"/></svg>Psychology</li>
    <li><svg class="svc-icon" viewBox="0 0 12 12"><circle cx="6" cy="6" r="6" fill="#111"/><circle cx="6" cy="5.5" r="2.4" fill="none" stroke="#fff"/><path d="M6 8v2" stroke="#fff"/></svg>Behavioural Therapy</li>
  </ul>
  <div class="contact-band">
    <span class="contact-item phone">
      <svg class="contact-icon" viewBox="0 0 13 13"><circle cx="6.5" cy="6.5" r="6.5" fill="#111"/><path d="M4.3 3.5l1.2 1.6-.7.8a5 5 0 0 0 2.3 2.3l.8-.7 1.6 1.2-.8 1.2C6.3 9.7 3.3 6.7 3.1 4.3z" fill="#fff"/></svg>
      1800 527 930
    </span>
    <span class="contact-item web">
      <svg class="contact-icon" viewBox="0 0 13 13"><circle cx="6.5" cy="6.5" r="6.5" fill="#111"/><circle cx="6.5" cy="6.5" r="4" fill="none" stroke="#fbd920" stroke-width=".9"/><ellipse cx="6.5" cy="6.5" rx="1.7" ry="4" fill="none" stroke="#fbd920" stroke-width=".9"/><path d="M2.5 6.5h8" stroke="#fbd920" stroke-width=".9"/></svg>
      www.tallbrook.com.au
    </span>
  </div>
</section>

<section class="parking-strip">
  <svg viewBox="0 0 567 34" width="567" height="34">
    <rect width="567" height="34" fill="var(--brand-yellow)"/>
    <polygon points="91,0 476,0 452,34 115,34" fill="var(--sign-white)"/>
    <polygon points="91,0 115,0 138,34 115,34" fill="var(--ink)"/>
    <polygon points="452,0 476,0 452,34 429,34" fill="var(--ink)"/>
  </svg>
  <div class="brand">
    <span class="brand-dot"></span>
    <span class="brand-name">Tallbrook</span>
  </div>
  <span class="parking-title">Visitor Parking 24/7</span>
</section>

<section class="dropoff-sign">
  <div class="yellow-half"></div>
  <div class="frame"></div>
  <div class="brand">
    <span class="brand-dot"></span>
    <span class="brand-name">Tallbrook</span>
  </div>
  <div class="dropoff-title">DROP-OFF<br>ZONE</div>
</section>

</body>
</html>
```